Rebrand stationary with recently completed logo design

Need new business cards, thank you cards, letterhead, envelopes and presentation folders. The designs will be sent to a separate production firm so I need the files to be print ready.

My contact info
Reno Vaskelind

Office 604-381-4756
Fax 604-318-5064

Email reno@glazeworks.ca
website www.glazeworks.ca

315-27140 62nd Avenue,
Langley, BC, V3K 2R8

Target Market(s)

Homeowners, businesses and contractors

Industry/Entity Type

Business

Font styles to use
Sans Serif

Colors
34a7d7

Requirements
Must have
• Like to have one side of the business card a solid color with the logo in all white. The side with all the text to be a white background
• I find the current blue on the front of the card with the white logo too dark.
Should not have
• Gradient colors

```html
<!DOCTYPE html>
<html lang="en">
<head>
<meta charset="utf-8">
<title>Thank You Card – Glazeworks</title>
<link rel="stylesheet" href="https://fonts.googleapis.com/css2?family=Kanit:ital,wght@1,500&family=Questrial&display=swap">
<style>
  :root {
    --brand-blue: #34a7d7;
    --frame-blue: #5bb8e0;
    --ink: #111111;
    --paper: #ffffff;
  }
  html, body {
    margin: 0;
    padding: 0;
    width: 1200px;
    height: 882px;
    overflow: hidden;
    background: var(--paper);
  }
  .thank-you-card {
    position: relative;
    width: 1200px;
    height: 882px;
  }
  .card-art {
    position: absolute;
    inset: 0;
    width: 1200px;
    height: 882px;
  }
  .card-frame {
    fill: none;
    stroke: var(--frame-blue);
    stroke-width: 2;
  }
  .headline {
    font-family: "Kanit", sans-serif;
    font-style: italic;
    font-weight: 500;
    font-size: 196px;
    fill: var(--brand-blue);
    letter-spacing: 2px;
  }
  .team-line {
    font-family: "Questrial", sans-serif;
    font-size: 29px;
    fill: var(--ink);
  }
  .slit-note {
    font-family: "Questrial", sans-serif;
    font-size: 33px;
    fill: var(--ink);
  }
  .card-slit {
    stroke: var(--ink);
    stroke-width: 2;
    stroke-dasharray: 8 8;
  }
</style>
</head>
<body>
  <main class="thank-you-card">
    <svg class="card-art" viewBox="0 0 1200 882" xmlns="http://www.w3.org/2000/svg">
      <rect class="card-frame" x="21" y="21" width="1158" height="838"/>

      <text class="headline" x="606" y="282" text-anchor="middle">Thank You</text>
      <text class="team-line" x="600" y="352" text-anchor="middle">from the team at Glazeworks</text>

      <line class="card-slit" x1="804" y1="506" x2="864" y2="566"/>
      <text class="slit-note" x="600" y="649" text-anchor="middle">Slits to hold your</text>
      <text class="slit-note" x="600" y="693" text-anchor="middle">business card</text>
      <line class="card-slit" x1="337" y1="741" x2="398" y2="804"/>
    </svg>
  </main>
</body>
</html>
```